Website redesign

We need a bold revamp of our website (http://www.brantocksparkworks.co.nz/)
which at the moment looks dated. We want a crisp, fresh and bold look. The background image behind web page can go. Open to complete new layout

Target Market(s)

Electrical contracting company- working in the domestic and commercial field

Coding

Coded - Design and coding required

Number of Pages Required

5+ page

Font styles to use
Sans Serif

Colors

Designer to choose colors to be used in the design.

```html
<!DOCTYPE html>
<html lang="en">
<head>
<meta charset="utf-8">
<title>Brantock Sparkworks</title>
<link href="https://fonts.googleapis.com/css2?family=Lato:ital,wght@0,400;0,700;0,900;1,700&family=Michroma&display=swap" rel="stylesheet">
<style>
:root{
  --red:#e10b0b;
  --red-bright:#ff1a1a;
  --black:#0d0d0d;
  --dark:#1b1b1b;
  --grey-text:#444;
  --light:#f2f2f2;
  --white:#ffffff;
  --footer-bar:#3a3a3a;
}
*{margin:0;padding:0;box-sizing:border-box}
html,body{width:1200px;height:3830px;overflow:hidden}
body{font-family:'Lato',Arial,sans-serif;color:var(--grey-text);background:var(--white);position:relative}
section,header,footer{position:absolute;left:0;width:1200px}
.abs{position:absolute}

/* header */
.site-header{top:0;height:166px;background:var(--white)}
.brand{left:69px;top:40px;color:var(--black);font-weight:900;font-size:44px;line-height:44px;letter-spacing:-1px}
.brand small{display:block;font-size:19px;font-weight:400;letter-spacing:2px;line-height:24px;margin-top:4px}
.brand-mark{display:inline-block;width:40px;height:26px;background:var(--red);vertical-align:top;margin-left:6px;margin-top:2px}
.call-free{left:660px;top:38px;text-align:center;font-size:13px;line-height:17px;color:var(--black);font-weight:700}
.call-free .label{color:var(--red);font-size:11px}
.follow{left:806px;top:38px;text-align:center}
.follow .label{color:var(--red);font-size:11px;font-weight:700}
.social{display:flex;gap:5px;margin-top:6px}
.social span{width:20px;height:20px;border-radius:50%;background:var(--black);display:block}
.divider-v{width:1px;height:56px;background:#ccc;top:34px}
.badge{left:960px;top:34px;width:60px;height:60px;border-radius:50%;background:#d9ecf5;border:3px solid #35a3d6}
.main-nav{left:567px;top:123px;width:608px;height:43px;background:var(--black);border-radius:22px 22px 0 0;display:flex;align-items:center;justify-content:space-around;padding:0 20px}
.main-nav a{color:var(--white);text-decoration:none;font-size:15px;font-weight:700}
.main-nav a.active{background:var(--red);padding:4px 18px;border-radius:12px}
.main-nav .sep{width:1px;height:20px;background:#666}

/* hero */
.hero{top:166px;height:498px;background:linear-gradient(100deg,#c8ccd2 0%,#8d96a3 35%,#4a5767 70%,#2b3644 100%)}
.hero h1{position:absolute;top:182px;width:100%;text-align:center;color:var(--white);font-weight:900;font-size:78px;letter-spacing:1px;line-height:80px}
.hero .tagline{position:absolute;top:262px;width:100%;text-align:center;color:var(--red-bright);font-weight:700;font-size:40px;letter-spacing:12px;line-height:44px}
.hero svg{position:absolute;top:222px}

/* section headings */
.heading{font-weight:900;color:var(--black);font-size:34px;display:flex;align-items:center;gap:12px;text-transform:uppercase}
.heading .sq{width:48px;height:32px;background:var(--red);display:block}
.heading-rule{width:56px;height:4px;background:var(--black);margin:16px auto 0}

/* about */
.about{top:664px;height:817px;background:var(--white)}
.about-photo{left:66px;top:71px;width:320px;height:674px;background:linear-gradient(160deg,#f4f4f4,#c9ccd0 55%,#8a8f96);border:1px solid #999}
.about-body{left:429px;top:82px;width:702px}
.about-body .lead{color:var(--red);font-style:italic;font-weight:700;font-size:19px;margin:38px 0 12px;border-top:2px solid #ddd;padding-top:20px}
.about-body p{font-size:14px;line-height:21px;margin-bottom:18px;text-align:justify}
.btn-dark{display:inline-block;background:var(--black);color:var(--white);font-size:11px;font-weight:700;width:138px;height:41px;line-height:41px;text-align:center;position:absolute;left:429px;top:704px}

/* services */
.services{top:1481px;height:975px;background:linear-gradient(180deg,#222 0%,#111 50%,#0a0a0a 100%)}
.services .heading{color:var(--white);justify-content:center;position:absolute;top:60px;width:100%}
.services .heading-rule{background:var(--white);position:absolute;top:113px;left:572px;margin:0}
.services-intro{position:absolute;top:148px;left:260px;width:680px;text-align:center;color:#e6e6e6;font-size:14px;line-height:21px}
.services-intro p{margin-bottom:18px}
.btn-light{position:absolute;left:521px;top:299px;width:138px;height:38px;background:var(--white);color:var(--black);font-size:11px;font-weight:700;text-align:center;line-height:38px}
.tile{position:absolute;width:378px;height:89px;background:linear-gradient(135deg,#9aa3ad,#4c5560);overflow:hidden}
.tile span{position:absolute;left:6px;bottom:4px;right:6px;font-family:'Michroma',Arial,sans-serif;color:var(--white);font-size:21px;line-height:30px;background:linear-gradient(90deg,rgba(0,0,0,.55),rgba(0,0,0,.2));padding-left:4px;white-space:nowrap}
.tile span.tight{font-size:18px;letter-spacing:-0.3px}

/* projects */
.projects{top:2456px;height:557px;background:var(--white)}
.projects .heading{justify-content:center;position:absolute;top:60px;width:100%}
.projects .heading-rule{position:absolute;top:113px;left:572px;margin:0}
.project-thumb{position:absolute;width:124px;height:124px;background:linear-gradient(135deg,#dfe5ea,#8ea0b2)}
.project-text{position:absolute;width:300px}
.project-text h3{color:var(--red);font-size:15px;font-weight:700;margin-bottom:14px}
.project-text p{font-size:12.5px;line-height:19px;margin-bottom:12px}
.project-text a{color:var(--black);font-size:12px;font-weight:700;text-decoration:none}
.project-text a b{color:var(--red)}

/* testimonials */
.testimonials{top:3013px;height:446px;background:var(--red)}
.testimonials .heading{color:var(--white);text-transform:none;font-weight:700;font-size:32px;justify-content:center;position:absolute;top:62px;width:100%}
.testimonials .heading .sq{background:var(--white);width:44px;height:30px}
.testimonials .heading-rule{background:var(--white);position:absolute;top:114px;left:572px;margin:0}
.quote-card{position:absolute;top:183px;width:307px;height:131px;border:2px solid var(--white);padding:26px 18px 0;color:var(--white)}
.quote-card .mark{position:absolute;top:-16px;left:16px;background:var(--red);font-size:40px;font-weight:900;line-height:34px;padding:0 4px}
.quote-card h4{font-size:13px;font-weight:700;margin-bottom:4px}
.quote-card p{font-size:12px;line-height:16px}
.person{position:absolute;display:flex;align-items:center;gap:10px;color:var(--white)}
.avatar{width:44px;height:44px;border-radius:50%;background:#f1c9c0;border:3px solid var(--white)}
.person b{font-size:12px;display:block}
.person span{font-size:11px;line-height:14px;display:block}
.testimonials svg{position:absolute;top:200px}

/* footer */
.site-footer{top:3459px;height:307px;background:var(--black);color:#ddd}
.foot-brand{left:69px;top:52px;color:var(--white);font-weight:900;font-size:50px;line-height:50px;letter-spacing:-1px}
.foot-brand small{display:block;font-size:20px;font-weight:400;letter-spacing:2px;line-height:26px}
.foot-about{left:69px;top:180px;width:190px;font-size:12px;line-height:15px;color:#ccc}
.foot-col{position:absolute;top:56px}
.foot-col h5{font-size:16px;font-weight:700;color:var(--red);letter-spacing:2px;padding-bottom:8px;border-bottom:1px solid #444;margin-bottom:14px}
.foot-col ul{list-style:none}
.foot-col li{font-size:14px;line-height:26px;color:#ddd}
.foot-col li:before{content:"› ";color:var(--red)}
.foot-col .line{font-size:12px;line-height:22px;display:flex;align-items:center;gap:6px;white-space:nowrap}
.foot-col .ic{width:9px;height:9px;background:var(--red);display:inline-block;flex:none}
.authorised{left:332px;top:56px;color:var(--white);font-size:17px;font-weight:700;line-height:19px}
.partner{width:110px;background:var(--white);margin-top:10px}
.foot-call{font-size:14px;font-weight:700;color:var(--white);line-height:20px;margin-top:30px}
.foot-call .num{font-size:22px;line-height:26px}
.foot-bar{top:3766px;height:64px;background:var(--footer-bar);color:#bbb;font-size:14px;text-align:center;line-height:64px}
</style>
</head>
<body>

<header class="site-header">
  <div class="abs brand">Brantock<span class="brand-mark"></span><small>SPARKWORKS</small></div>
  <div class="abs call-free"><div class="label">CALL US FREE</div>0800 47 19 62<br>(06)552 7140</div>
  <div class="abs divider-v" style="left:790px"></div>
  <div class="abs follow"><div class="label">FOLLOW US</div><div class="social"><span></span><span></span><span></span><span></span></div></div>
  <div class="abs divider-v" style="left:940px"></div>
  <div class="badge abs" role="img" aria-label="Partner certification badge"></div>
  <nav class="abs main-nav">
    <a class="active">Home</a><span class="sep"></span>
    <a>About us</a><span class="sep"></span>
    <a>Services</a><span class="sep"></span>
    <a>Projects</a><span class="sep"></span>
    <a>Contact us</a>
  </nav>
</header>

<section class="hero" role="img" aria-label="Photo of an electrician working on network cabling in a server cabinet">
  <h1>YOUR TEXT HERE</h1>
  <div class="tagline">YOUR TAG LINE HERE</div>
  <svg style="left:76px" width="26" height="52" viewBox="0 0 26 52"><path d="M22 4 L4 26 L22 48" fill="none" stroke="#fff" stroke-width="4"/></svg>
  <svg style="left:1098px" width="26" height="52" viewBox="0 0 26 52"><path d="M4 4 L22 26 L4 48" fill="none" stroke="#fff" stroke-width="4"/></svg>
</section>

<section class="about">
  <div class="abs about-photo" role="img" aria-label="Photo of an electrician in a hard hat fitting a switchboard"></div>
  <div class="abs about-body">
    <div class="heading"><span class="sq"></span>About us</div>
    <div class="lead">Proudly serving our local community for over 20 years</div>
    <p>Brantock Sparkworks is a leading electrical installation and maintenance company based in Ravenmouth, but servicing all New Zealand. We are proud to be locally owned and operated. With over 15 employees, we are a very professional qualified and experienced team of technicians and support staff.</p>
    <p>Brantock Sparkworks was established in 1991 and does it all, from supplying and changing light bulbs, comprehensive whole house electrical design and installation, to commercial and large scale industrial consultation, implementation and servicing.</p>
    <p>With over 20 years' experience in providing our customers with personalized service for their home electrical needs, individual lighting plans, experienced advise on renovations, heating and cooling requirements for home comfort, security systems and cameras, and providing the most up to date equipment and knowledge of energy efficiency and all electrical legislation.</p>
    <p>As Ravenmouth's top Koruvent accredited installers and Ravenmouth's ONLY member of The Climate Installer Guild (CIG) of New Zealand we aim to continue to provide the Ravenmouth region with the highest possible quality of professional service.</p>
    <p>Our goal is to provide you with the best possible electrical advice and service. In everything we do, from consultation and design to finishing the job, our commitment to providing reliable, high quality services is evident. Our electrical technicians are on call 24 hour, 7 days a week.</p>
    <p>Let us provide the peace of mind that comes with knowing that all workmanship is guaranteed and done to meet all the regulations and standards with integrity, experience and dedication.</p>
  </div>
  <div class="btn-dark">READ MORE</div>
</section>

<section class="services">
  <div class="heading"><span class="sq"></span>Our Services</div>
  <div class="heading-rule"></div>
  <div class="services-intro">
    <p>Brantock Sparkworks offers all the domestic and commercial electrical services you would expect from an electrical firm, but with dedicated technicans in specialist electrical areas they have the more technical ability and experience than your average sparky.</p>
    <p>If you can't find what you are looking for in the appropriate sections listed, simply contact us on<br>0800 47 19 62 and we will be able to help you out.</p>
  </div>
  <div class="btn-light">READ MORE</div>
  <div class="tile" style="left:378px;top:370px;height:84px;width:373px" role="img" aria-label="Electrical wiring photo"><span>Electrical</span></div>
  <div class="tile" style="left:179px;top:480px" role="img" aria-label="Appliance testing photo"><span>Appliance Testing</span></div>
  <div class="tile" style="left:577px;top:480px" role="img" aria-label="Alarm keypad photo"><span>Alarms</span></div>
  <div class="tile" style="left:179px;top:587px" role="img" aria-label="Security camera photo"><span>Security Cameras</span></div>
  <div class="tile" style="left:577px;top:587px" role="img" aria-label="Heat pump unit photo"><span>Heat Pumps</span></div>
  <div class="tile" style="left:179px;top:694px" role="img" aria-label="Fire alarm photo"><span>Fire/Smoke</span></div>
  <div class="tile" style="left:577px;top:694px" role="img" aria-label="Building inspection photo"><span class="tight">IQP Building Compliance</span></div>
  <div class="tile" style="left:179px;top:799px" role="img" aria-label="Network data cabling photo"><span>Phone/Data</span></div>
  <div class="tile" style="left:577px;top:799px" role="img" aria-label="Satellite dish photo"><span class="tight">TV - Satellite/Aerial</span></div>
</section>

<section class="projects">
  <div class="heading"><span class="sq"></span>Our Projects</div>
  <div class="heading-rule"></div>

  <div class="project-thumb" style="left:66px;top:163px" role="img" aria-label="Commercial building project photo"></div>
  <div class="project-text" style="left:232px;top:163px">
    <h3>Lorem ipsum dolor sit amet</h3>
    <p>Lorem ipsum dolor sit amet, consectetur adipiscing elit. Quid autem habent admirationis,prope accesseris. Lorem ipsum dolor sit amet, consectetur adipiscing elit.</p>
    <a>Read more <b>»</b></a>
  </div>

  <div class="project-thumb" style="left:636px;top:160px;height:116px" role="img" aria-label="Network cabling project photo"></div>
  <div class="project-text" style="left:804px;top:150px">
    <h3>Lorem ipsum dolor sit amet</h3>
    <p>Lorem ipsum dolor sit amet, consectetur adipiscing elit. Quid autem habent admirationis,prope accesseris. Lorem ipsum dolor sit amet, consectetur adipiscing elit.</p>
    <a>Read more <b>»</b></a>
  </div>

  <div class="project-thumb" style="left:66px;top:347px;height:128px" role="img" aria-label="Switchboard wiring project photo"></div>
  <div class="project-text" style="left:232px;top:347px">
    <h3>Lorem ipsum dolor sit amet</h3>
    <p>Lorem ipsum dolor sit amet, consectetur adipiscing elit. Quid autem habent admirationis,prope accesseris. Lorem ipsum dolor sit amet, consectetur adipiscing elit.</p>
    <a>Read more <b>»</b></a>
  </div>

  <div class="project-thumb" style="left:636px;top:337px;height:122px" role="img" aria-label="Ceiling smoke detector project photo"></div>
  <div class="project-text" style="left:804px;top:337px">
    <h3>Lorem ipsum dolor sit amet</h3>
    <p>Lorem ipsum dolor sit amet, consectetur adipiscing elit. Quid autem habent admirationis,prope accesseris. Lorem ipsum dolor sit amet, consectetur adipiscing elit.</p>
    <a>Read more <b>»</b></a>
  </div>
</section>

<section class="testimonials">
  <div class="heading"><span class="sq"></span>Clients Testimonials</div>
  <div class="heading-rule"></div>
  <svg style="left:74px" width="24" height="48" viewBox="0 0 24 48"><path d="M20 4 L4 24 L20 44" fill="none" stroke="#fff" stroke-width="4"/></svg>
  <svg style="left:1102px" width="24" height="48" viewBox="0 0 24 48"><path d="M4 4 L20 24 L4 44" fill="none" stroke="#fff" stroke-width="4"/></svg>

  <div class="quote-card" style="left:263px">
    <span class="mark">“</span>
    <h4>Highly Professional Team</h4>
    <p>Lorem ipsum dolor sit amet, consectetur adipiscing elit. Quid autem habent admirationis, cum prope accesseris? An hoc usque quaque, aliter in vita?</p>
    <div class="person" style="top:142px;left:-2px">
      <div class="avatar" role="img" aria-label="Client portrait"></div>
      <div><b>MR DELACOURT</b><span>Sales manager at Larkfield Freight</span><span>President at Tavora MP</span></div>
    </div>
  </div>

  <div class="quote-card" style="left:633px">
    <span class="mark">“</span>
    <h4>Highly Professional Team</h4>
    <p>Lorem ipsum dolor sit amet, consectetur adipiscing elit. Quid autem habent admirationis, cum prope accesseris? An hoc usque quaque, aliter in vita?</p>
    <div class="person" style="top:142px;left:-2px">
      <div class="avatar" role="img" aria-label="Client portrait"></div>
      <div><b>MR DELACOURT</b><span>Sales manager at Larkfield Freight</span><span>President at Tavora MP</span></div>
    </div>
  </div>
</section>

<footer class="site-footer">
  <div class="abs foot-brand">Brantock<small>SPARKWORKS</small></div>
  <div class="abs foot-about">Lorem ipsum dolor sit amet, consectetur adipiscing elit. Quid autem habent admirationis, cum prope accesseris</div>

  <div class="abs authorised">We are<br>authorised<br>installers for:
    <div class="partner" style="height:40px"></div>
    <div class="partner" style="height:50px;border-radius:4px"></div>
  </div>

  <div class="foot-col" style="left:516px;width:160px">
    <h5>QUICK LINKS</h5>
    <ul><li>Home</li><li>About us</li><li>Services</li><li>Projects</li><li>Contact us</li></ul>
  </div>

  <div class="foot-col" style="left:728px;width:190px">
    <h5>CONTACT</h5>
    <div style="font-size:12px;line-height:17px;margin-bottom:10px">14 Kerrow Street,<br>Ravenmouth 7316</div>
    <div class="line"><span class="ic"></span>0800 47 19 62</div>
    <div class="line"><span class="ic"></span>(06)552 7141</div>
    <div class="line" style="font-size:11px"><span class="ic"></span>office@brantocksparkworks.co.nz</div>
    <div class="line" style="font-size:11px"><span class="ic"></span>www.brantocksparkworks.co.nz</div>
  </div>

  <div class="foot-col" style="left:960px;width:170px">
    <h5>FOLLOW US ON</h5>
    <div class="social"><span style="background:#fff"></span><span style="background:#fff"></span><span style="background:#fff"></span><span style="background:#fff"></span></div>
    <div class="foot-call">CALL US ON<div class="num">0800 47 19 62</div><div class="num">(06)552 7140</div></div>
  </div>
</footer>

<div class="abs foot-bar" style="left:0;width:1200px">© 2016 Brantock Sparkworks | Privacy Policy | User Agreement</div>

</body>
</html>
```